Velvet Lantern - listen to podcasts from around the world

http://randompodcasts.com/Velvet Lantern lets you listen to randomly selected podcasts from around the world. You can filter the podcasts by language. The power of randomness allows you to escape filter bubbles and echo chambers and discover issues and perspectives that you never knew existed. The current website offers basic functionality and is only a demo. Don't assume that anything in the current "design" should stay in place. The goal of the design should be to make it as easy as possible to understand what the app offers, to listen to new podcasts, and to skip to the next podcast. The service will be offered both as mobile apps and directly on the website. We expect that most users will be on mobile devices which is why we are focusing on the mobile/web app design.In addition to the current functionality, the app should also offer search (allowing the user to listen to podcasts that match given keywords), allow the user to easily subscribe to the current podcast and show the profile picture of the current podcast.

Target Market(s)

People interested in podcasts, all around the world

Colors

Designer to choose colors to be used in the design.

Requirements
Must have
• The main challenge is how to communicate the concept of the app to the user. Podcasts are randomly selected and the user just skips to the next one when he/she wants to. The ability to filter podcasts by language is important but no other filters are needed. The point is to use the power of random selection to explore new surprising content.
Nice to have
• The app/website is targeting a global audience. The less reliant the design is on written language, the better.

```html
<!DOCTYPE html>
<html lang="en">
<head>
<meta charset="utf-8">
<title>Velvet Lantern – About & Menu screens</title>
<link href="https://fonts.googleapis.com/css2?family=Alegreya+Sans:wght@500;700&family=Source+Sans+3:wght@300;400&family=Raleway:wght@300;400&family=Noto+Sans+Oriya&display=swap" rel="stylesheet">
<style>
  :root{
    --page:#ffffff;
    --bar:#ffffff;
    --bar-ink:#b9b9bd;
    --about-top:#5b4548;
    --about-bottom:#262438;
    --ink:#ffffff;
    --ink-soft:#d9d4da;
    --accent:#f2577f;
    --pink-top:#df56a3;
    --pink-bottom:#f8607a;
    --drawer:#000000;
    --drawer-ink:#d6d6d6;
    --muted:#4a4a4a;
  }
  *{box-sizing:border-box;margin:0;padding:0}
  html,body{width:1200px;height:1200px;overflow:hidden;background:var(--page)}
  body{position:relative;font-family:"Source Sans 3",sans-serif}

  .screen{position:absolute;overflow:hidden;border-radius:10px}

  /* About screen */
  .about{left:206px;top:46px;width:395px;height:1107px;
    background:linear-gradient(180deg,var(--about-top) 0%,var(--about-bottom) 100%)}
  .topbar{position:absolute;left:0;top:0;width:100%;height:94px;background:var(--bar)}
  .clock{position:absolute;left:32px;top:16px;font:400 16px "Source Sans 3",sans-serif;color:#666}
  .status{position:absolute;right:22px;top:20px}
  .topbar .menu-icon{position:absolute;left:24px;top:58px}
  .topbar .more{position:absolute;right:22px;top:55px}
  .page-title{position:absolute;left:0;right:0;top:50px;text-align:center;
    font:400 21px "Raleway",sans-serif;letter-spacing:2px;color:var(--bar-ink)}

  .brand{position:absolute;left:0;right:0;top:116px;text-align:center;
    font:700 21px "Alegreya Sans",sans-serif;letter-spacing:3px;color:var(--ink)}
  .quote{position:absolute;left:0;right:0;top:164px;text-align:center;
    font:300 26px/31px "Raleway",sans-serif;letter-spacing:1.5px;color:var(--ink)}
  .tagline{position:absolute;left:24px;right:20px;top:332px;
    font:300 21px/29px "Source Sans 3",sans-serif;color:var(--accent)}
  .copy{position:absolute;left:24px;right:22px;
    font:300 12.6px/16.8px "Source Sans 3",sans-serif;color:var(--ink-soft)}
  .copy.one{top:412px}
  .copy.two{top:513px}

  .team{position:absolute;left:0;right:0;top:628px;list-style:none}
  .member{position:relative;height:104px}
  .avatar{position:absolute;left:35px;top:1px;width:51px;height:51px;border-radius:50%}
  .avatar.dark{background:radial-gradient(circle at 50% 40%,#6b5b4c,#2f3a2c)}
  .avatar.light{background:radial-gradient(circle at 50% 40%,#c9d3da,#e8c46a)}
  .member h3{position:absolute;left:112px;top:0;font:400 18px "Source Sans 3",sans-serif;color:var(--ink)}
  .member p{position:absolute;left:112px;top:23px;width:240px;
    font:300 12.4px/17px "Source Sans 3",sans-serif;color:var(--ink-soft)}

  .closing{position:absolute;left:30px;right:30px;top:955px;text-align:center;
    font:400 10.6px/17px "Source Sans 3",sans-serif;letter-spacing:.8px;color:var(--ink-soft)}
  .footer-rule{position:absolute;top:1050px;height:1px;width:89px;background:#8c8794}
  .footer-rule.left{left:34px}.footer-rule.right{left:272px}
  .social{position:absolute;left:0;right:0;top:1042px;text-align:center;
    font:400 10px "Source Sans 3",sans-serif;color:var(--ink)}

  /* Menu screen */
  .player{left:650px;top:302px;width:393px;height:851px;
    background:linear-gradient(180deg,var(--pink-top) 0%,var(--pink-bottom) 100%)}
  .player .topbar{height:94px}
  .player .status{right:14px;top:20px}
  .player .more{position:absolute;right:20px;top:56px}
  .cover{position:absolute;border-radius:8px}
  .cover.main{left:50px;top:170px;width:293px;height:303px;background:linear-gradient(160deg,#7a3a5a,#3b2240)}
  .cover.side{left:362px;top:214px;width:40px;height:259px;background:linear-gradient(180deg,#b66a86,#f26c8d)}
  .cover.prev{left:-10px;top:214px;width:40px;height:259px;background:#8a3b55}
  .seek{position:absolute;left:22px;top:547px;width:349px;height:2px;background:rgba(255,255,255,.6)}
  .seek-fill{position:absolute;left:22px;top:547px;width:80px;height:2px;background:#fff}
  .knob{position:absolute;left:86px;top:533px;width:30px;height:30px;border-radius:50%;background:#fff}
  .time{position:absolute;top:563px;font:400 10px "Source Sans 3",sans-serif;color:#fff}
  .time.start{left:22px}.time.end{right:22px}
  .controls{position:absolute;left:0;top:612px;width:393px;height:22px}
  .chip{position:absolute;top:667px;width:111px;height:31px;border-radius:4px;background:#fff;
    text-align:center;font:400 12px/31px "Source Sans 3",sans-serif;color:#999}
  .episode{position:absolute;left:22px;top:714px;width:349px;height:160px;border-radius:8px;background:#fff}
  .episode dt{position:absolute;left:33px;font:400 13px "Raleway",sans-serif;letter-spacing:1px;color:#bbb}
  .episode dd{position:absolute;left:119px;font:400 13px "Raleway","Noto Sans Oriya",sans-serif;letter-spacing:1px;color:#888;white-space:nowrap}
  .episode hr{position:absolute;left:20px;top:84px;width:310px;border:0;border-top:1px solid #e3e3e3}

  .drawer{position:absolute;left:0;top:0;width:338px;height:851px;
    background:linear-gradient(180deg,var(--drawer) 0%,var(--drawer) 14%,rgba(0,0,0,.9) 30%,rgba(12,4,10,.93) 100%)}
  .drawer .menu-icon{position:absolute;left:22px;top:55px}
  .nav{list-style:none;position:absolute;left:0;top:0;width:100%}
  .nav li{position:absolute;left:26px;display:flex;align-items:center;gap:18px;
    font:400 14.5px "Raleway",sans-serif;letter-spacing:1.4px;color:#9a9a9a}
  .nav li.current{color:var(--drawer-ink)}
  .faint{position:absolute;left:130px;top:400px;font:400 12px/20px "Raleway",sans-serif;color:rgba(255,255,255,.09);letter-spacing:1px;text-align:center}
</style>
</head>
<body>

<section class="screen about" aria-label="About screen">
  <header class="topbar">
    <span class="clock">9:41</span>
    <svg class="status" width="70" height="14" viewBox="0 0 70 14" aria-hidden="true">
      <g fill="#888"><rect x="0" y="9" width="2.5" height="4"/><rect x="4" y="7" width="2.5" height="6"/><rect x="8" y="5" width="2.5" height="8"/><rect x="12" y="3" width="2.5" height="10"/></g>
      <path d="M22 6a9 9 0 0 1 13 0M25 9a5 5 0 0 1 7 0" stroke="#888" stroke-width="1.6" fill="none"/><circle cx="28.5" cy="11.5" r="1.3" fill="#888"/>
      <rect x="46" y="2" width="21" height="10" rx="2" fill="none" stroke="#888"/><rect x="47.5" y="3.5" width="18" height="7" rx="1" fill="#888"/>
    </svg>
    <svg class="menu-icon" width="17" height="12" viewBox="0 0 17 12" aria-hidden="true"><g stroke="#aaa" stroke-width="1.2"><path d="M0 1h17M0 4.5h17M3 8h14M0 11.5h17"/></g></svg>
    <h1 class="page-title">About Us</h1>
    <svg class="more" width="4" height="18" viewBox="0 0 4 18" aria-hidden="true"><g fill="none" stroke="#e9a0b2"><circle cx="2" cy="2" r="1.5"/><circle cx="2" cy="9" r="1.5"/><circle cx="2" cy="16" r="1.5"/></g></svg>
  </header>

  <h2 class="brand">Velvet Lantern</h2>
  <p class="quote">"VELVET<br>LANTERN<br>IS NOT IN THE<br>RADIO."<br>WE KNOW.</p>
  <p class="tagline">Over 1 trillion pixels shared. What are you working on?</p>
  <p class="copy one">Tens of millions of people look for design inspiration and feedback on Pixelhaven. We help players like you share small screenshots (shots) to show off your current projects, boost your portfolio, and love what you do—no matter what kind of creative professional you are.</p>
  <p class="copy two">Founded in 2009, we are a bootstrapped and profitable company helping design talent share, grow, and get hired by over 40,000 of today’s most innovative brands around the world.</p>

  <ul class="team">
    <li class="member"><div class="avatar dark" role="img" aria-label="Team member portrait"></div><h3>Tomas Ferrell</h3><p>A guy that loves design, writing comics, veggie burgersand making silly music.</p></li>
    <li class="member"><div class="avatar light" role="img" aria-label="Team member portrait"></div><h3>Tomas Ferrell</h3><p>A guy that loves design, writing comics, veggie burgersand making silly music.</p></li>
    <li class="member"><div class="avatar dark" role="img" aria-label="Team member portrait"></div><h3>Tomas Ferrell</h3><p>A guy that loves design, writing comics, veggie burgersand making silly music.</p></li>
  </ul>

  <p class="closing">We believe that creative collaboration can happen anywhere and want our team to work where they feel most comfortable and inspired.</p>
  <span class="footer-rule left"></span>
  <p class="social">Chirpline · Friendsheet</p>
  <span class="footer-rule right"></span>
</section>

<section class="screen player" aria-label="Player screen with open menu">
  <header class="topbar">
    <svg class="status" width="26" height="12" viewBox="0 0 26 12" aria-hidden="true"><rect x="1" y="1" width="22" height="10" rx="2" fill="none" stroke="#888"/><rect x="2.5" y="2.5" width="19" height="7" rx="1" fill="#888"/></svg>
    <svg class="more" width="4" height="18" viewBox="0 0 4 18" aria-hidden="true"><g fill="none" stroke="#bbb"><circle cx="2" cy="2" r="1.5"/><circle cx="2" cy="9" r="1.5"/><circle cx="2" cy="16" r="1.5"/></g></svg>
  </header>

  <div class="cover prev" role="img" aria-label="Previous podcast artwork"></div>
  <div class="cover main" role="img" aria-label="Current podcast artwork"></div>
  <div class="cover side" role="img" aria-label="Next podcast artwork"></div>

  <span class="seek"></span><span class="seek-fill"></span><span class="knob"></span>
  <span class="time start">0:12</span><span class="time end">2.12</span>

  <svg class="controls" viewBox="0 0 393 22" aria-hidden="true">
    <path d="M30 18l-7-7a4 4 0 0 1 7-4 4 4 0 0 1 7 4z" fill="#fff"/>
    <path d="M96 5v12M108 5l-9 6 9 6z" stroke="#fff" fill="none" stroke-width="1.3"/>
    <path d="M189 4l11 7-11 7z" stroke="#fff" fill="none" stroke-width="1.3"/>
    <path d="M293 5v12M281 5l9 6-9 6z" stroke="#fff" fill="none" stroke-width="1.3"/>
    <path d="M364 3v11M359 9l5 5 5-5M356 15v4h16v-4" stroke="#fff" fill="none" stroke-width="1.4"/>
  </svg>

  <span class="chip" style="left:22px">echo 1</span>
  <span class="chip" style="left:141px">echo 2</span>
  <span class="chip" style="left:261px">echo 3</span>

  <dl class="episode">
    <dt style="top:24px">Episode</dt><dd style="top:24px">856 ସେମାନଙ୍କ ଜୋତା ପିନ୍ଧି ଚାଲିବା</dd>
    <dd style="top:58px">Walking in their shose</dd>
    <hr>
    <dt style="top:95px">Published</dt><dd style="top:95px">4 days ago</dd>
  </dl>

  <nav class="drawer" aria-label="Main menu">
    <svg class="menu-icon" width="19" height="14" viewBox="0 0 19 14" aria-hidden="true"><g stroke="var(--accent)" stroke-width="1.6"><path d="M0 1h19M0 5h19M3 9h16M0 13h19"/></g></svg>
    <div class="faint">Our Silver Sparrow<br>stories from quiet towns<br>told by the locals</div>
    <ul class="nav">
      <li style="top:117px"><svg width="13" height="13" viewBox="0 0 13 13" aria-hidden="true"><path d="M1.5 6L6.5 1.5 11.5 6v6h-10z M5 12V8h3v4" fill="none" stroke="#bbb"/></svg>Home</li>
      <li class="current" style="top:185px"><svg width="13" height="13" viewBox="0 0 13 13" aria-hidden="true"><circle cx="6.5" cy="6.5" r="5.5" fill="none" stroke="#ddd"/><circle cx="6.5" cy="6.5" r="2.5" fill="#ddd"/></svg>Velvet Lantern</li>
      <li style="top:254px"><svg width="13" height="13" viewBox="0 0 13 13" aria-hidden="true"><circle cx="6.5" cy="6.5" r="4.5" fill="none" stroke="#bbb" stroke-dasharray="2 1.2"/><circle cx="6.5" cy="6.5" r="1.8" fill="none" stroke="#bbb"/></svg>Setting</li>
      <li style="top:321px"><svg width="13" height="13" viewBox="0 0 13 13" aria-hidden="true"><circle cx="6.5" cy="6.5" r="5.5" fill="none" stroke="#bbb"/><path d="M4.8 5a1.8 1.8 0 1 1 2.4 1.6c-.5.2-.7.6-.7 1.2" fill="none" stroke="#bbb"/><circle cx="6.5" cy="9.8" r=".6" fill="#bbb"/></svg>FAQ</li>
      <li style="top:389px"><svg width="13" height="13" viewBox="0 0 13 13" aria-hidden="true"><circle cx="5" cy="4" r="2.3" fill="none" stroke="#bbb"/><path d="M1 11a4 4 0 0 1 8 0M9 2a2 2 0 0 1 0 4M10.5 8a3 3 0 0 1 2 3" fill="none" stroke="#bbb"/></svg>About Us</li>
    </ul>
  </nav>
</section>

</body>
</html>
```